Hip Music Management Co. BIz Card

I have a logo (attached) the back side of the card should the full logo on the entire card- that's it. The front side of the card should show the logo somewhere, keeping with the 4 different shades of blue. The front side of the card can be a white background with logo and colored typeface for all info. Pretty simple.

Target Market(s)

I manage and produce a whole bunch of major label and indie artists.

Industry/Entity Type

Management

Contact Information for Business Card

Velmarra Sound Collective (logo)
Dale Wortheny
President
www.velmarrasoundcollective.com
dale@velmarrasoundcollective.com
+1 415.287.6192
718 Copperfield Lane
Ashgrove Falls, OR 97412

Requirements
Must have
• Entire logo on back side. White background on front- unless you provide something more interesting.
Nice to have
• On the front of the card if you choose a white backgound, if possible take my logo without the blue background (over white) that would be cool.

```html
<!DOCTYPE html>
<html lang="en">
<head>
<meta charset="utf-8">
<title>Velmarra Sound Collective – Business Card</title>
<link rel="stylesheet" href="https://fonts.googleapis.com/css2?family=Montserrat:wght@600;700&family=Questrial&display=swap">
<style>
  :root {
    --backdrop: #e9ebef;
    --card-white: #fbfbfc;
    --royal-blue: #2d62d3;
    --deep-blue: #2a55b5;
    --sky-blue: #4aaee6;
    --teal: #34cfa8;
    --ink: #3a4050;
  }
  * { box-sizing: border-box; margin: 0; padding: 0; }
  html, body {
    width: 1200px; height: 1000px; overflow: hidden;
    background: var(--backdrop);
  }
  .canvas { position: relative; width: 1200px; height: 1000px; }
  .card {
    position: absolute; left: 250px; width: 700px; height: 400px;
    border-radius: 6px; overflow: hidden;
    box-shadow: 0 6px 18px rgba(20, 30, 60, 0.18);
  }
  .card--front { top: 75px; background: var(--card-white); }
  .card--back { top: 525px; background: var(--royal-blue); }

  .front-wave { position: absolute; inset: 0; width: 700px; height: 400px; }

  .wordmark {
    position: absolute; left: 48px; top: 38px;
    font-family: "Montserrat", sans-serif; font-weight: 700;
    font-size: 30px; line-height: 1.05; color: var(--teal);
    letter-spacing: 0.5px;
  }
  .contact-list {
    position: absolute; left: 48px; top: 104px;
    list-style: none;
    font-family: "Questrial", sans-serif; font-size: 17px;
    line-height: 26px; color: var(--ink);
  }
  .contact-list .label { color: var(--deep-blue); margin-right: 6px; }

  .person { position: absolute; right: 46px; top: 262px; text-align: right; }
  .person__name {
    font-family: "Montserrat", sans-serif; font-weight: 700;
    font-size: 27px; color: var(--royal-blue); letter-spacing: 0.5px;
  }
  .person__title {
    font-family: "Questrial", sans-serif; font-size: 25px;
    color: var(--teal); margin-top: 2px;
  }

  .back-wordmark {
    position: absolute; inset: 0;
    display: flex; align-items: center; justify-content: center;
    text-align: center;
    font-family: "Montserrat", sans-serif; font-weight: 700;
    font-size: 46px; line-height: 1.1; color: var(--teal);
    letter-spacing: 1px;
  }
</style>
</head>
<body>
<main class="canvas">
  <section class="card card--front" aria-label="Business card front">
    <svg class="front-wave" viewBox="0 0 700 400" aria-hidden="true">
      <path d="M0 280 C 120 266, 190 312, 300 346 C 380 370, 450 376, 520 400 L 0 400 Z" fill="var(--royal-blue)"/>
    </svg>
    <div class="wordmark">Velmarra Sound Collective</div>
    <ul class="contact-list">
      <li><span class="label">W:</span>www.velmarrasoundcollective.com</li>
      <li><span class="label">E:</span>dale@velmarrasoundcollective.com</li>
      <li><span class="label">P:</span>+1 415.287.6192</li>
      <li><span class="label">A:</span>718 Copperfield Lane</li>
      <li>Ashgrove Falls, OR 97412</li>
    </ul>
    <div class="person">
      <div class="person__name">DALE WORTHENY</div>
      <div class="person__title">president</div>
    </div>
  </section>

  <section class="card card--back" aria-label="Business card back">
    <div class="back-wordmark">Velmarra<br>Sound Collective</div>
  </section>
</main>
</body>
</html>
```